New web design for a service provider in the medical field

We are looking for a new design for our website. We are a company that repairs and sells medical endoscopes. Our customers include doctors and hospitals. Our current website can be found at https://lumenfix.example/en/lumenfix-english.
We need a new web design (without programming) for the following 3 pages:
-Startpage https://lumenfix.example/en/lumenfix-english/
-Used endoscopes https://lumenfix.example/en/used-endoscopes/
-Purchase https://lumenfix.example/en/purchase/
The design should be modern and stylish.
The blue color of the logo should be reflected on the page, but not too intrusive.
I have uploaded the images from the header. If more images are needed, let me know and I will upload them.

Target Market(s)
Doctors and hospitals

```html
<!DOCTYPE html>
<html lang="en">
<head>
<meta charset="utf-8">
<title>LumenFix – Endoscope Repair</title>
<link href="https://fonts.googleapis.com/css2?family=Poppins:wght@400;500;600;700;800&display=swap" rel="stylesheet">
<style>
:root{
  --blue:#1f6fb8;
  --blue-dark:#1562a8;
  --blue-deep:#0f5697;
  --blue-light:#e8f0f8;
  --ink:#2b2f36;
  --muted:#555c66;
  --line:#e3e8ee;
  --white:#fff;
}
*{box-sizing:border-box;margin:0;padding:0}
html,body{width:1200px;height:3167px;overflow:hidden}
body{font-family:'Poppins',sans-serif;color:var(--ink);background:var(--white);position:relative}
.abs{position:absolute}
a{color:inherit;text-decoration:none}

/* top bar */
.topbar{position:absolute;left:0;top:0;width:1200px;height:25px;background:var(--blue);color:#fff;font-size:8px;font-weight:500}
.topbar .tag{left:200px;top:7px}
.topbar .links{left:543px;top:7px;display:flex;gap:11px}
.topbar .contact{left:748px;top:4px;display:flex;gap:16px;align-items:center}
.topbar .contact span{display:flex;align-items:center;gap:6px}
.topbar .ic{width:14px;height:14px;border:1px solid #fff;border-radius:50%}
.topbar .lang{width:14px;height:14px;border-radius:50%;background:linear-gradient(#222 33%,#d22 33% 66%,#f5c400 66%)}

/* header */
.header{position:absolute;left:0;top:25px;width:1200px;height:73px;background:#fff}
.brand{left:200px;top:27px;display:flex;align-items:center;gap:8px;font-weight:700;font-size:16px;color:var(--blue-deep)}
.brand i{width:12px;height:12px;border-radius:50%;background:var(--blue)}
.nav{left:350px;top:38px;display:flex;gap:22px;font-size:8.5px;font-weight:500;color:#333}
.nav .active{color:var(--blue);border-bottom:1px solid var(--blue)}
.btn-solid{background:var(--blue);color:#fff;border-radius:20px;font-weight:600;font-size:8.5px;text-align:center}
.header .btn-solid{left:911px;top:30px;width:89px;height:28px;line-height:28px}

/* hero */
.hero{position:absolute;left:0;top:98px;width:1200px;height:575px;overflow:hidden;
  background:linear-gradient(100deg,#6f9fbf 0%,#3f87b5 45%,#2b7ab0 70%,#5c9ec4 100%)}
.hero h1{left:200px;top:130px;font-size:36px;line-height:38px;font-weight:800;color:#fff;letter-spacing:.2px}
.hero p{left:200px;top:220px;width:470px;font-size:11.2px;line-height:18.5px;color:#fff}
.hero .btn-solid{left:200px;top:316px;width:126px;height:28px;line-height:28px;font-size:8.5px}
.hero .arrow{left:258px;top:420px;color:#fff;font-size:18px}
.hero svg.wave{position:absolute;left:0;bottom:0}

/* intro */
h2.title{font-size:25px;line-height:31px;font-weight:600;color:var(--blue)}
.underline{width:58px;height:3px;background:var(--blue);border-radius:2px;position:relative}
.underline::after{content:"";position:absolute;left:64px;top:0;width:3px;height:3px;background:var(--blue);box-shadow:5px 0 0 var(--blue);border-radius:50%}
.body-text{font-size:10px;line-height:16.5px;color:var(--muted)}
.btn-outline{border:1.5px solid var(--blue);color:var(--blue);border-radius:20px;font-size:8.5px;font-weight:600;text-align:center}
.intro h2{left:200px;top:713px;width:370px}
.intro .underline{left:200px;top:843px}
.intro .p1{left:200px;top:866px;width:390px}
.intro .p2{left:200px;top:931px;width:390px}
.intro .btn-outline{left:200px;top:1003px;width:88px;height:28px;line-height:26px}
.intro .photo{left:610px;top:705px;width:390px;height:340px;background:linear-gradient(135deg,#eceef0,#c9ced3 60%,#8e959c)}

/* brands */
.brands{position:absolute;left:0;top:1109px;width:1200px;height:137px;background:var(--blue-light)}
.brands .badge{top:37px;width:186px;height:63px;background:#fff;box-shadow:0 2px 6px rgba(0,0,0,.08)}
.badge .mark{position:absolute;left:43px;top:24px;width:100px;height:15px;border-radius:3px}

/* services */
.services h2{left:200px;top:1300px}
.services .underline{left:200px;top:1338px}
.services .lead{left:200px;top:1355px;width:800px}
.card{background:#fff;border:1px solid var(--line);box-shadow:0 2px 8px rgba(0,0,0,.05)}
.card .icon{position:absolute;top:-37px;left:10px;width:72px;height:72px;border-radius:50%;background:#fff;border:1px solid var(--line);display:flex;align-items:center;justify-content:center}
.card .icon.filled{background:var(--blue);border:none}
.card h3{position:absolute;left:11px;top:50px;font-size:16px;font-weight:600;color:var(--blue)}
.card h4{position:absolute;left:11px;top:75px;font-size:9px;font-weight:600;color:#333}
.card p{position:absolute;left:11px;top:98px;width:230px;font-size:9px;line-height:15px;color:var(--muted)}
.card .go{position:absolute;left:14px;bottom:-14px;width:28px;height:28px;border-radius:50%;background:#fff;border:1px solid var(--line);color:var(--blue);text-align:center;line-height:26px;font-size:12px}
.card .go.filled{background:var(--blue);color:#fff;border:none}

/* faulty */
.faulty .photo{left:200px;top:1725px;width:391px;height:313px;background:radial-gradient(circle at 55% 40%,#8fb8ec,#3d74c8 45%,#1d4aa0)}
.faulty .panel{left:591px;top:1725px;width:409px;height:313px;background:var(--blue-light)}
.faulty h2{left:627px;top:1795px;font-size:22px}
.faulty .underline{left:627px;top:1831px}
.faulty .sub{left:628px;top:1842px;font-size:12px;font-weight:500;color:#333}
.faulty .small{left:628px;top:1907px;font-size:10px;color:#444}
.faulty .btn-outline{left:628px;top:1930px;width:100px;height:28px;line-height:26px}

/* cause */
.cause .panel{left:200px;top:2064px;width:409px;height:347px;background:var(--blue-light)}
.cause .photo{left:609px;top:2064px;width:391px;height:347px;background:linear-gradient(140deg,#d9dde0,#7e8790 45%,#2f5fbf 75%,#1c3f9a)}
.cause h2{left:237px;top:2080px;font-size:22px}
.cause .underline{left:237px;top:2116px}
.cause ul{left:237px;top:2135px;list-style:none;width:340px}
.cause li{position:relative;padding-left:21px;margin-bottom:11.5px}
.cause li svg{position:absolute;left:0;top:3px}
.cause li b{display:block;font-size:11px;font-weight:500;color:var(--blue);line-height:16px}
.cause li span{display:block;font-size:9.5px;color:#444;line-height:14.5px}

/* decision */
.decision h2{left:200px;top:2465px}
.decision .underline{left:200px;top:2503px}
.dcard{top:2563px;width:255px;height:139px}
.dcard .icon{position:absolute;left:15px;top:-27px;width:52px;height:52px;border-radius:50%;background:#fff;display:flex;align-items:center;justify-content:center}
.dcard h3{position:absolute;left:12px;top:52px;font-size:11.5px;font-weight:600;color:var(--blue)}
.dcard p{position:absolute;left:12px;top:71px;width:232px;font-size:9px;line-height:15px;color:var(--muted)}
.slide-btn{top:2617px;width:30px;height:30px;border-radius:50%;text-align:center;line-height:28px;font-size:13px}

/* cta */
.cta{position:absolute;left:0;top:2765px;width:1200px;height:100px;background:var(--blue)}
.cta h2{left:200px;top:32px;font-size:32px;font-weight:800;color:#fff}
.cta .btn-white{left:825px;top:29px;width:175px;height:36px;line-height:36px;background:#fff;color:var(--blue);border-radius:20px;font-size:11px;font-weight:600;text-align:center;letter-spacing:.5px}

/* footer */
.footer{position:absolute;left:0;top:2865px;width:1200px;height:255px;background:var(--blue-dark);color:#fff}
.footer h5{top:42px;font-size:13px;font-weight:600}
.finfo{left:200px;top:74px;font-size:9px;line-height:12.5px}
.finfo .row{display:flex;gap:10px;align-items:flex-start;margin-bottom:14px}
.finfo .ic{width:26px;height:26px;border:1px solid rgba(255,255,255,.7);border-radius:50%;flex:none;display:flex;align-items:center;justify-content:center}
.flinks{left:405px;top:76px;font-size:10px;line-height:24.3px}
.flinks .u{text-decoration:underline}
.map{left:609px;top:75px;width:391px;height:158px;background:linear-gradient(135deg,#f3f3f1,#e5e7ea)}
.totop{left:1147px;top:210px;width:40px;height:40px;border-radius:50%;background:var(--blue-deep);text-align:center;line-height:38px;font-size:14px}
.bottombar{position:absolute;left:0;top:3120px;width:1200px;height:47px;background:var(--blue-deep);color:#fff;font-size:9px}
.bottombar .copy{left:200px;top:18px}
.bottombar .soc{top:12px;width:24px;height:24px;border-radius:50%;border:1px solid rgba(255,255,255,.8)}
</style>
</head>
<body>

<div class="topbar">
  <div class="abs tag">Cause the outcome matters</div>
  <div class="abs links"><span>PICK-UP ORDER</span><span>ABOUT US</span><span>CONTACT US</span></div>
  <div class="abs contact">
    <span><i class="ic"></i><u>info@lumenfix.example</u></span>
    <span><i class="ic"></i>+49 4000 555 120-0</span>
    <i class="lang"></i>
  </div>
</div>

<header class="header">
  <div class="abs brand"><i></i>LumenFix</div>
  <nav class="abs nav">
    <span class="active">HOME</span><span>ENDOSCOPE REPAIR</span><span>USED ENDOSCOPES ⌵</span><span>ENDOSCOPY SYSTEMS</span><span>ENDOSCOPY ACCESSORIES ⌵</span>
  </nav>
  <a class="abs btn-solid">PURCHASE</a>
</header>

<section class="hero" role="img" aria-label="Medical team in a clinic holding a flexible endoscope">
  <h1 class="abs">PUT YOUR ENDOSCOPE IN<br>RELIABLE HANDS!</h1>
  <p class="abs">LumenFix GmbH is specialized in repairing and saling flexible endoscopes along with accessories and consumables. We offer endoscopes, processors, light sources, accessories and much more – with a focus on the manufacturers Kestrel, Norvik and Halden.</p>
  <a class="abs btn-solid">PURCHASE REQUEST</a>
  <div class="abs arrow">↓</div>
  <svg class="wave" width="1200" height="180" viewBox="0 0 1200 180"><path d="M0 180 L0 150 C120 120 200 60 330 95 C430 122 480 30 560 8 C640 -10 700 60 780 90 C880 128 1000 140 1200 172 L1200 180 Z" fill="#fff"/></svg>
</section>

<section class="intro">
  <h2 class="abs title">Endoscope Repairs And Second Hand Endoscopes From LumenFix – Cause the outcome matters!</h2>
  <div class="abs underline"></div>
  <p class="abs body-text p1">LumenFix is a privileged partner for the start-up facility or optimisation of existing healthcare facilities, doctor's offices and hospitals. The quality and reliability of our products and our offered service are our best advertisement!</p>
  <p class="abs body-text p2">As a result of optimised processes and highly qualified specialists in our company, we can work very quickly and with high quality for your benefit of least possible restrictions in your doctor's office or in your hospital.</p>
  <a class="abs btn-outline">ABOUT US</a>
  <div class="abs photo" role="img" aria-label="Close-up of an endoscope control head with angulation knobs"></div>
</section>

<section class="brands">
  <div class="abs badge" style="left:302px"><div class="mark" style="background:#1b2a8f"></div></div>
  <div class="abs badge" style="left:507px"><div class="mark" style="background:#c8202b"></div></div>
  <div class="abs badge" style="left:712px"><div class="mark" style="background:#222"></div></div>
</section>

<section class="services">
  <h2 class="abs title">Your Future - Our Service</h2>
  <div class="abs underline"></div>
  <p class="abs body-text lead">LumenFix GmbH is specialised in the repair and sale of Kestrel, Norvik and Halden flexible medical endoscopes. As a service-oriented company, we are at your side with our knowledge and skills!</p>

  <div class="abs card" style="left:200px;top:1451px;width:255px;height:197px">
    <div class="icon"><svg width="34" height="34" viewBox="0 0 34 34" fill="none" stroke="#1f6fb8" stroke-width="1.6"><circle cx="17" cy="17" r="10"/><circle cx="17" cy="17" r="4"/><path d="M17 3v4M17 27v4M3 17h4M27 17h4M7 7l3 3M24 24l3 3M27 7l-3 3M10 24l-3 3"/></svg></div>
    <h3>Repair</h3><h4>ENDOSCOPE REPAIR SERVICE</h4>
    <p>Manufacturer-independent we repair and maintain endoscopes, individual components (e.g. processors or light sources), accessories and peripherals of the manufacturers Kestrel, Norvik and Halden.</p>
    <div class="go">→</div>
  </div>
  <div class="abs card" style="left:473px;top:1451px;width:255px;height:197px">
    <div class="icon filled"><svg width="34" height="34" viewBox="0 0 34 34" fill="none" stroke="#fff" stroke-width="1.6"><path d="M6 18 L18 6 H28 V16 L16 28 Z"/><circle cx="23" cy="11" r="2"/></svg></div>
    <h3>Sale</h3><h4>USED ENDOSCOPES</h4>
    <p>Our regular stock includes refurbished gastroscopes, coloscopes, bronchoscopes, cystoscopes and duodenoscopes from the well-known manufacturers Kestrel, Norvik and Halden.</p>
    <div class="go filled">→</div>
  </div>
  <div class="abs card" style="left:746px;top:1451px;width:254px;height:197px">
    <div class="icon"><svg width="34" height="34" viewBox="0 0 34 34" fill="none" stroke="#1f6fb8" stroke-width="1.6"><rect x="5" y="6" width="24" height="22" rx="2"/><path d="M5 11h24M9 16h16v8H9z"/></svg></div>
    <h3>Purchase</h3><h4>USED ENDOSCOPES</h4>
    <p>We are very interested in buying your old endoscopes – even defective and dismantled! We offer fair conditions! Please contact us for a purchase offer!</p>
    <div class="go">→</div>
  </div>
</section>

<section class="faulty">
  <div class="abs photo" role="img" aria-label="Endoscope tip with lens and light on a blue fabric background"></div>
  <div class="abs panel"></div>
  <h2 class="abs title">Faulty Endoscope?</h2>
  <div class="abs underline"></div>
  <p class="abs sub">We ensure quick and smooth repairs!</p>
  <p class="abs small">Simple place a</p>
  <a class="abs btn-outline">PICK-UP ORDER</a>
</section>

<section class="cause">
  <div class="abs panel"></div>
  <div class="abs photo" role="img" aria-label="Gloved hands holding an endoscope handle during servicing"></div>
  <h2 class="abs title">Cause The Outcome Matters!</h2>
  <div class="abs underline"></div>
  <ul class="abs">
    <li><svg width="12" height="10" viewBox="0 0 12 10"><path d="M1 5l3 3 7-7" fill="none" stroke="#1f6fb8" stroke-width="1.5"/></svg><b>One Company For Everyone</b><span>We are a service provider for doctors and hospitals!</span></li>
    <li><svg width="12" height="10" viewBox="0 0 12 10"><path d="M1 5l3 3 7-7" fill="none" stroke="#1f6fb8" stroke-width="1.5"/></svg><b>Experience Characterises Us</b><span>Our team has many years of experience in the business field!</span></li>
    <li><svg width="12" height="10" viewBox="0 0 12 10"><path d="M1 5l3 3 7-7" fill="none" stroke="#1f6fb8" stroke-width="1.5"/></svg><b>The Product is Close To Our Hearts</b><span>We repair and sell second hand, flexible endoscopes!</span></li>
    <li><svg width="12" height="10" viewBox="0 0 12 10"><path d="M1 5l3 3 7-7" fill="none" stroke="#1f6fb8" stroke-width="1.5"/></svg><b>Guaranteed Service</b><span>You receive a six-month warranty on all repairs!</span></li>
    <li><svg width="12" height="10" viewBox="0 0 12 10"><path d="M1 5l3 3 7-7" fill="none" stroke="#1f6fb8" stroke-width="1.5"/></svg><b>Quality Not Quantity</b><span>Reliability and durability instead of inferior replacements!</span></li>
    <li><svg width="12" height="10" viewBox="0 0 12 10"><path d="M1 5l3 3 7-7" fill="none" stroke="#1f6fb8" stroke-width="1.5"/></svg><b>Services For Everyone</b><span>Our service includes the manufacturers Kestrel, Norvik and Halden!</span></li>
  </ul>
</section>

<section class="decision">
  <h2 class="abs title">LumenFix GmbH, Your Decision For Your Future</h2>
  <div class="abs underline"></div>
  <div class="abs card dcard" style="left:200px">
    <div class="icon"><svg width="24" height="24" viewBox="0 0 24 24" fill="none" stroke="#1f6fb8" stroke-width="1.6"><path d="M4 20L14 10M10 4l4 4-3 3-4-4zM20 20L8 8"/></svg></div>
    <h3>FAST REPAIRS</h3>
    <p>Keep potential disruptions in your doctor's office or in your hospital at minimum as a result of optimized processes and highly qualified specialists in our company.</p>
  </div>
  <div class="abs card dcard" style="left:473px">
    <div class="icon"><svg width="24" height="24" viewBox="0 0 24 24" fill="none" stroke="#1f6fb8" stroke-width="1.6"><path d="M3 17c4 0 6 3 10 3s6-2 8-4M12 3v9M9 6h4a2 2 0 010 4h-2"/></svg></div>
    <h3>HIGHLY COST EFFICIENT</h3>
    <p>Benefit from our first class recommendations and implementation by our experienced staff. Our goals is to find the best solutions together with you at the best lowest price point.</p>
  </div>
  <div class="abs card dcard" style="left:746px;width:254px">
    <div class="icon"><svg width="24" height="24" viewBox="0 0 24 24" fill="none" stroke="#1f6fb8" stroke-width="1.6"><path d="M3 11l9-8 9 8M5 9v12h14V9M10 21v-6h4v6"/></svg></div>
    <h3>ON-SITE SERVICE</h3>
    <p>We will gladly pay you a visit to to carry out analysis and repairs on site. Due to our many years of experience – it doesn't get any faster (within a 250 km range)</p>
  </div>
  <div class="abs slide-btn" style="left:150px;color:#1f6fb8">←</div>
  <div class="abs slide-btn" style="left:1008px;background:#1f6fb8;color:#fff">→</div>
</section>

<section class="cta">
  <h2 class="abs">HOW CAN WE HELP YOU?</h2>
  <a class="abs btn-white">SEND US A MESSAGE!</a>
</section>

<footer class="footer">
  <h5 class="abs" style="left:200px">CONATCT INFO</h5>
  <h5 class="abs" style="left:405px">QUICK LINKS</h5>
  <div class="abs finfo">
    <div class="row"><span class="ic"><svg width="10" height="12" viewBox="0 0 10 12"><path d="M5 11S1 7 1 4.5a4 4 0 018 0C9 7 5 11 5 11z" fill="none" stroke="#fff"/></svg></span><span>Lindenweg 12<br>21400 Musterfeld<br>Germany</span></div>
    <div class="row"><span class="ic"><svg width="10" height="10" viewBox="0 0 10 10"><path d="M2 1l2 2-1 1.5c1 1.5 2 2.5 3.5 3.5L8 7l2 2-1.5 1C5 9.5 1 5 1 2z" fill="none" stroke="#fff"/></svg></span><span><u>+49 4000 555 120-0</u><br>+49 4000 555 120-1 (FAX)</span></div>
    <div class="row"><span class="ic"><svg width="11" height="8" viewBox="0 0 11 8"><rect x=".5" y=".5" width="10" height="7" fill="none" stroke="#fff"/><path d="M.5.5l5 4 5-4" fill="none" stroke="#fff"/></svg></span><span style="padding-top:7px">info@lumenfix.example</span></div>
    <div class="row"><span class="ic"><svg width="11" height="11" viewBox="0 0 11 11"><circle cx="5.5" cy="5.5" r="4.5" fill="none" stroke="#fff"/><path d="M5.5 3v3h2" fill="none" stroke="#fff"/></svg></span><span>Monday – Friday<br>08:00 – 20:00</span></div>
  </div>
  <div class="abs flinks">
    <div class="u">informations</div><div>About Us</div><div>Contact Us</div><div>Tos</div><div>Copyrights</div><div>Privacy policy</div>
  </div>
  <div class="abs map" role="img" aria-label="Street map showing the company location"></div>
  <div class="abs totop">↑</div>
</footer>

<div class="bottombar">
  <div class="abs copy">© Copyright 2022 <u>LumenFix</u>. All Rights Reserved.</div>
  <div class="abs soc" style="left:942px;background:#fff"></div>
  <div class="abs soc" style="left:975px"></div>
</div>

</body>
</html>
```